"Harbor Constructors" is a residential building company and needs a new business card design and may re

We would like a redesign based on the existing logo, and would like to see a new font as well. We are bespoke home builders who build sustainable energy efficient homes.

Industry/Entity Type

Construction

Contact Information for Business Card

Business card size 40mm x 90mm

Colors

Designer to choose colors to be used in the design.

```html
<!DOCTYPE html>
<html lang="en">
<head>
<meta charset="utf-8">
<title>Harbor Constructors – Business Card</title>
<link rel="stylesheet" href="https://fonts.googleapis.com/css2?family=Roboto:wght@400;700;900&display=swap">
<style>
  :root {
    --navy: #233a7d;
    --orange: #ee7d22;
    --white: #ffffff;
    --ink: #6b6f78;
    --stage: #e9eaee;
  }
  * { box-sizing: border-box; margin: 0; padding: 0; }
  html, body { width: 1200px; height: 786px; overflow: hidden; }
  body {
    background: var(--stage);
    font-family: "Roboto", Arial, sans-serif;
    position: relative;
  }
  .card {
    position: absolute;
    top: 278px;
    width: 520px;
    height: 231px;
    box-shadow: 0 6px 18px rgba(20, 30, 60, 0.18);
  }
  .card--front { left: 60px; background: var(--white); }
  .card--back  { left: 620px; background: var(--navy); }

  /* Wordmark */
  .wordmark {
    display: flex;
    align-items: center;
    gap: 10px;
  }
  .wordmark__square {
    width: 14px; height: 14px;
    background: var(--orange);
  }
  .wordmark__name {
    font-weight: 900;
    letter-spacing: 0.04em;
    text-transform: uppercase;
    line-height: 1;
  }
  .card--front .wordmark { position: absolute; left: 28px; top: 26px; }
  .card--front .wordmark__name { color: var(--navy); font-size: 24px; }

  .card--back .wordmark {
    position: absolute; left: 0; right: 0; top: 0; bottom: 0;
    justify-content: center;
  }
  .card--back .wordmark__name { color: var(--white); font-size: 30px; }

  /* Person */
  .person { position: absolute; left: 28px; top: 78px; }
  .person__name {
    color: var(--navy); font-weight: 700; font-size: 14px;
    text-transform: uppercase; letter-spacing: 0.02em;
  }
  .person__role { color: var(--ink); font-size: 11px; margin-top: 2px; }
  .person__rule {
    width: 14px; height: 2px; background: var(--orange);
    margin-top: 8px;
  }

  /* Contacts */
  .contacts {
    position: absolute; left: 28px; top: 138px;
    list-style: none; color: var(--ink); font-size: 11px;
  }
  .contacts li {
    display: flex; align-items: center; gap: 7px;
    margin-bottom: 5px;
  }
  .contacts svg { width: 10px; height: 10px; flex: none; }

  /* Company details */
  .company {
    position: absolute; right: 28px; bottom: 22px;
    text-align: right; color: var(--ink); font-size: 11px; line-height: 1.45;
  }
  .company__reg { color: var(--navy); }
</style>
</head>
<body>

  <section class="card card--front" aria-label="Business card front">
    <div class="wordmark">
      <span class="wordmark__name">Harbor Constructors</span>
    </div>

    <div class="person">
      <p class="person__name">Daniel Marsh</p>
      <p class="person__role">Founder</p>
      <div class="person__rule"></div>
    </div>

    <ul class="contacts">
      <li>
        <svg viewBox="0 0 10 10" aria-hidden="true"><path d="M2 1 L4 1 L4.6 3 L3.4 3.8 Q4.4 5.8 6.2 6.6 L7 5.4 L9 6 L9 8 Q8.6 9 7.6 9 Q1 8.4 1 2.4 Q1 1 2 1 Z" fill="#ee7d22"/></svg>
        0400 555 018
      </li>
      <li>
        <svg viewBox="0 0 10 10" aria-hidden="true"><rect x="0.5" y="2" width="9" height="6.5" fill="#ee7d22"/><path d="M0.5 2 L5 5.6 L9.5 2" fill="none" stroke="#fff" stroke-width="0.9"/></svg>
        daniel@harborconstructors.com.au
      </li>
      <li>
        <svg viewBox="0 0 10 10" aria-hidden="true"><circle cx="5" cy="5" r="4.5" fill="#ee7d22"/><path d="M0.5 5 H9.5 M5 0.5 Q2.5 5 5 9.5 M5 0.5 Q7.5 5 5 9.5" fill="none" stroke="#fff" stroke-width="0.7"/></svg>
        www.harborconstructors.com.au
      </li>
    </ul>

    <div class="company">
      <p class="company__reg">Registration-40718</p>
      <p>ABN: 12 345 678 901</p>
      <p>PO Box 2210 Northgate</p>
      <p>LPO Eastvale WA 6000</p>
    </div>
  </section>

  <section class="card card--back" aria-label="Business card back">
    <div class="wordmark">
      <span class="wordmark__square"></span>
      <span class="wordmark__name">Harbor Constructors</span>
    </div>
  </section>

</body>
</html>
```